iron deficiency anemia - educational reference paper

looking for an educational paper/poster 8x11 or no larger than 11x14 that lists the most common foods with pictures and limited words a super rough outline attached - I wrote the words of the pictures (but would like to have the actual pictures of these items) I would like in roughly the same order
for the pictures for fatigue, headache....can be drawings or cartoons
double sided or single sided (which ever fits) see attached for categories (3 of them)

Target Market(s)

educational for people with limited education - thus not much wording

Requirements
Must have
• pictures, simple design

```html
<!DOCTYPE html>
<html lang="en">
<head>
<meta charset="utf-8">
<title>Iron Deficiency Anemia – Reference Sheet</title>
<link rel="stylesheet" href="https://fonts.googleapis.com/css2?family=Montserrat:wght@600;700;800&family=Open+Sans:wght@400;600&display=swap">
<style>
  :root{
    --backdrop:#a4a5ac;
    --paper:#ffffff;
    --red:#c2172f;
    --red-deep:#7d0d1c;
    --red-dark:#4a0610;
    --ink:#111111;
    --grey-band:#d9d9db;
    --grey-ring:#c9c9cc;
    --black-bar:#141414;
  }
  *{box-sizing:border-box;margin:0;padding:0}
  html,body{width:1200px;height:1200px;overflow:hidden}
  body{background:var(--backdrop);position:relative;font-family:"Open Sans",Arial,sans-serif;color:var(--ink)}

  .sheet{position:absolute;top:260px;height:674px;background:var(--paper);overflow:hidden;box-shadow:0 6px 14px rgba(0,0,0,.25)}
  .sheet--front{left:56px;width:520px}
  .sheet--back{left:622px;width:523px}

  /* ---------- FRONT ---------- */
  .front-header{position:absolute;left:0;top:0;width:520px;height:240px}
  .front-title{position:absolute;left:14px;top:8px;font-family:"Montserrat",sans-serif;font-weight:800;font-size:36px;line-height:1.1;color:#fff;letter-spacing:.3px}
  .portrait{position:absolute;left:298px;top:60px;width:156px;height:156px;border-radius:50%;border:6px solid var(--grey-ring);background:radial-gradient(circle at 50% 40%,#f4efe9,#d8d2cb)}
  .foods-heading{position:absolute;left:12px;top:152px;font-family:"Montserrat",sans-serif;font-weight:700;font-size:22px;line-height:1.15;color:var(--red)}
  .foods-rule{position:absolute;left:0;top:238px;width:230px;height:2px;background:var(--red)}

  .food-list{position:absolute;top:274px;list-style:none;font-size:12.5px;line-height:15.3px;color:var(--ink)}
  .food-list .gap{height:12px}
  .food-list--meat{left:81px}
  .food-list--legume{left:236px}
  .food-list--greens{left:401px}
  .food-list .gap-small{height:8px}

  .food-icons{position:absolute;border-radius:50%}
  .icon-col{position:absolute;top:272px}

  .veg-photo{position:absolute;left:262px;top:566px;width:258px;height:108px;background:linear-gradient(180deg,#5f9a3a 0%,#3f7d2a 45%,#c9462d 80%,#e3b53d 100%);border-radius:40px 0 0 0}

  .info-bar{position:absolute;left:0;top:618px;width:306px;height:36px;background:var(--black-bar);border-radius:0 18px 18px 0;display:flex;align-items:center;padding-left:18px;gap:10px;color:#fff}
  .info-bar__label{font-family:"Montserrat",sans-serif;font-weight:700;font-size:16px;letter-spacing:.3px}
  .info-bar__icon{width:22px;height:22px}
  .info-bar__number{font-family:"Montserrat",sans-serif;font-weight:700;font-size:17px}
  .front-strip{position:absolute;left:0;top:654px;width:300px;height:10px;background:var(--red)}

  /* ---------- BACK ---------- */
  .more-info{position:absolute;left:22px;top:22px;font-family:"Montserrat",sans-serif;font-weight:700;font-size:18px}
  .web-pill{position:absolute;left:228px;top:19px;width:264px;height:33px;border-radius:17px;background:var(--red);display:flex;align-items:center;padding-left:8px;gap:12px;color:#fff;font-family:"Montserrat",sans-serif;font-weight:700;font-size:18px}
  .web-pill svg{width:22px;height:22px}

  .symptoms-tab{position:absolute;left:0;top:70px;width:190px;height:72px;background:var(--red);color:#fff;padding:12px 0 0 20px;font-family:"Montserrat",sans-serif}
  .symptoms-tab__small{font-size:15px;font-weight:600;letter-spacing:.3px;line-height:1}
  .symptoms-tab__big{font-size:29px;font-weight:800;line-height:1.15;letter-spacing:.5px}
  .signs-band{position:absolute;left:190px;top:70px;width:333px;height:72px;background:var(--grey-band);display:flex;align-items:center;justify-content:center;font-family:"Montserrat",sans-serif;font-weight:800;font-size:25px;color:var(--red);letter-spacing:.3px}
  .signs-pointer{position:absolute;left:346px;top:141px;width:0;height:0;border-left:14px solid transparent;border-right:14px solid transparent;border-top:14px solid var(--grey-band)}

  .symptom-panel{position:absolute;left:0;top:142px;width:180px;height:512px;background:linear-gradient(180deg,#050505 0%,#1a0307 45%,var(--red-deep) 75%,var(--red) 100%)}
  .symptom-list{position:absolute;left:20px;top:172px;list-style:none;color:#fff;font-family:"Montserrat",sans-serif;font-weight:600;font-size:17px;line-height:20px;letter-spacing:.3px}
  .symptom-list li{display:flex;gap:14px;align-items:flex-start;margin-bottom:21px}
  .symptom-list svg{flex:none;width:22px;height:22px;margin-top:-2px}

  .signs-frame{position:absolute;left:212px;top:193px;width:290px;height:161px;border:1.5px solid #e39aa5;background:#fff}
  .sign-photo{position:absolute}

  .rest-scene{position:absolute;left:0;top:0;width:523px;height:674px}
  .back-strip{position:absolute;left:0;top:658px;width:523px;height:16px;background:var(--red)}
</style>
</head>
<body>

<!-- FRONT: foods -->
<section class="sheet sheet--front">
  <svg class="front-header" viewBox="0 0 520 240" aria-hidden="true">
    <defs>
      <linearGradient id="cellRed" x1="0" y1="0" x2="1" y2="1">
        <stop offset="0" stop-color="#8e0f20"/>
        <stop offset=".5" stop-color="#b3182c"/>
        <stop offset="1" stop-color="#6e0a17"/>
      </linearGradient>
    </defs>
    <path d="M0 0H520V232C490 205 455 160 410 140C320 100 170 98 0 130Z" fill="#bdbdc0"/>
    <path d="M0 0H520V222C490 195 455 150 410 130C320 92 170 90 0 120Z" fill="url(#cellRed)"/>
  </svg>
  <h1 class="front-title">IRON DEFICIENCY<br>ANEMIA</h1>
  <div class="portrait" role="img" aria-label="Photo of a woman holding an apple and a pear"></div>

  <h2 class="foods-heading">Common<br>Foods in<br>Your Community</h2>
  <div class="foods-rule"></div>

  <svg class="icon-col" style="left:38px" width="24" height="380" role="img" aria-label="Small photos of meats, fish and staple foods">
    <circle cx="12" cy="11" r="11" fill="#9a8f86"/><circle cx="12" cy="34" r="11" fill="#5f7a4a"/>
    <circle cx="12" cy="57" r="11" fill="#7a6a5c"/><circle cx="12" cy="80" r="11" fill="#a88a74"/>
    <circle cx="12" cy="103" r="11" fill="#5d8a62"/><circle cx="12" cy="126" r="11" fill="#8c8f94"/>
    <circle cx="12" cy="149" r="11" fill="#6b4f3c"/><circle cx="12" cy="172" r="11" fill="#c29070"/>
    <circle cx="12" cy="195" r="11" fill="#d49a6a"/><circle cx="12" cy="218" r="11" fill="#c58a5a"/>
    <circle cx="12" cy="241" r="11" fill="#d9d0c4"/><circle cx="12" cy="264" r="11" fill="#8a6e56"/>
    <circle cx="12" cy="287" r="11" fill="#b28a5e"/><circle cx="12" cy="310" r="11" fill="#c23a2a"/>
  </svg>
  <ul class="food-list food-list--meat">
    <li>Sheep/lamb</li><li>Goose</li><li>Whale</li><li>Pig/pork</li><li>Duck</li>
    <li>Chicken</li><li>Clams</li><li>Cuttlefish</li><li>Bear</li><li>Sardines</li>
    <li>Shrimp</li><li>Turkey</li><li>Halibut</li><li class="gap" aria-hidden="true"></li>
    <li>Bagel</li><li>Egg</li><li>Mushrooms</li><li>Potatoe</li><li>Tortilla</li>
    <li>Blackberry</li><li>Tomatoe</li>
  </ul>

  <svg class="icon-col" style="left:172px" width="48" height="300" role="img" aria-label="Photos of beans, peas and seeds">
    <circle cx="24" cy="22" r="22" fill="#4f9a34"/><circle cx="24" cy="70" r="22" fill="#c9a45a"/>
    <circle cx="24" cy="118" r="22" fill="#b6ad7c"/><circle cx="24" cy="166" r="22" fill="#e0a022"/>
    <circle cx="24" cy="212" r="20" fill="#a77b4c"/><circle cx="24" cy="248" r="12" fill="#cfc3a4"/>
  </svg>
  <ul class="food-list food-list--legume">
    <li>Lentil</li><li>Yellow bean</li><li>Lima bean</li><li>Pumpkin seen</li><li>Squab</li>
    <li>Pigeon pea</li><li>Fava bean</li><li>Sesame seed</li><li>Aduzki bean</li><li>Cranberry bean</li>
    <li>Masa</li><li>Split peas</li><li>Sunflower seed</li><li>Chickpeas</li><li>Nuts</li>
    <li>Winged bean</li><li>Rice bran</li>
  </ul>

  <svg class="icon-col" style="left:350px" width="42" height="300" role="img" aria-label="Photos of beans, grains and green vegetables">
    <circle cx="20" cy="20" r="19" fill="#c9c2b2"/><circle cx="20" cy="64" r="19" fill="#2c2a28"/>
    <circle cx="20" cy="108" r="19" fill="#7a8a3a"/><circle cx="20" cy="158" r="19" fill="#3f8a30"/>
    <circle cx="20" cy="206" r="19" fill="#4d9440"/><circle cx="20" cy="250" r="19" fill="#d0702e"/>
  </svg>
  <ul class="food-list food-list--greens">
    <li>White bean</li><li>Kidney bean</li><li>Cowpea</li><li>Black bean</li><li>Mung bean</li>
    <li>Natto</li><li>Teff</li><li>Amaranth</li><li>Yardlong bean</li><li>Chili/pink bean</li>
    <li class="gap-small" aria-hidden="true"></li>
    <li>Spinach</li><li>Beet</li><li>Brussle sprouts</li><li>Collard greens</li><li>Broccoli</li>
    <li>Carrot</li><li>Califlower</li>
  </ul>

  <div class="veg-photo" role="img" aria-label="Photo of fresh vegetables"></div>

  <div class="info-bar">
    <span class="info-bar__label">MORE INFO</span>
    <svg class="info-bar__icon" viewBox="0 0 22 22" aria-hidden="true">
      <circle cx="11" cy="11" r="10" fill="none" stroke="var(--red)" stroke-width="2"/>
      <path d="M7.5 6.5l2 -.5 1.2 2.6-1.2 1c.6 1.3 1.5 2.2 2.8 2.8l1-1.2 2.6 1.2-.5 2c-4 .4-8.3-3.9-7.9-7.9z" fill="var(--red)"/>
    </svg>
    <span class="info-bar__number">555 014 272</span>
  </div>
  <div class="front-strip"></div>
</section>

<!-- BACK: symptoms and signs -->
<section class="sheet sheet--back">
  <svg class="rest-scene" viewBox="0 0 523 674" aria-hidden="true">
    <defs>
      <linearGradient id="restTone" x1="0" y1="0" x2="1" y2="1">
        <stop offset="0" stop-color="#ece6e2"/>
        <stop offset=".6" stop-color="#d9ccc6"/>
        <stop offset="1" stop-color="#bfb2ae"/>
      </linearGradient>
    </defs>
  </svg>

  <p class="more-info">For More Info:</p>
  <div class="web-pill">
    <svg viewBox="0 0 22 22" aria-hidden="true">
      <circle cx="11" cy="11" r="10" fill="#fff"/>
      <circle cx="11" cy="11" r="6" fill="none" stroke="var(--red)" stroke-width="1.4"/>
      <ellipse cx="11" cy="11" rx="2.6" ry="6" fill="none" stroke="var(--red)" stroke-width="1.2"/>
      <path d="M5 11h12" stroke="var(--red)" stroke-width="1.2"/>
    </svg>
    <span>www.ironwise.org</span>
  </div>

  <div class="symptoms-tab">
    <div class="symptoms-tab__small">SYMPTOMS OF</div>
    <div class="symptoms-tab__big">ANEMIA</div>
  </div>
  <div class="signs-band">SIGNS OF ANEMIA</div>
  <div class="signs-pointer"></div>

  <div class="symptom-panel"></div>
  <ul class="symptom-list">
    <li><svg viewBox="0 0 22 22" aria-hidden="true"><rect x="1" y="4" width="16" height="16" fill="none" stroke="var(--red)" stroke-width="2"/><path d="M5 11l4 5 11-14" fill="none" stroke="var(--red)" stroke-width="3"/></svg><span>FATIGUE</span></li>
    <li><svg viewBox="0 0 22 22" aria-hidden="true"><rect x="1" y="4" width="16" height="16" fill="none" stroke="var(--red)" stroke-width="2"/><path d="M5 11l4 5 11-14" fill="none" stroke="var(--red)" stroke-width="3"/></svg><span>HEADACHE</span></li>
    <li><svg viewBox="0 0 22 22" aria-hidden="true"><rect x="1" y="4" width="16" height="16" fill="none" stroke="var(--red)" stroke-width="2"/><path d="M5 11l4 5 11-14" fill="none" stroke="var(--red)" stroke-width="3"/></svg><span>DIZZINESS</span></li>
    <li><svg viewBox="0 0 22 22" aria-hidden="true"><rect x="1" y="4" width="16" height="16" fill="none" stroke="var(--red)" stroke-width="2"/><path d="M5 11l4 5 11-14" fill="none" stroke="var(--red)" stroke-width="3"/></svg><span>BLURRY<br>VISION</span></li>
    <li><svg viewBox="0 0 22 22" aria-hidden="true"><rect x="1" y="4" width="16" height="16" fill="none" stroke="var(--red)" stroke-width="2"/><path d="M5 11l4 5 11-14" fill="none" stroke="var(--red)" stroke-width="3"/></svg><span>MUSCLE<br>WEAKNESS</span></li>
  </ul>

  <div class="signs-frame">
    <div class="sign-photo" style="left:8px;top:6px;width:112px;height:58px;background:linear-gradient(180deg,#e9d6cf,#caa59a)" role="img" aria-label="Photo of pale, spoon-shaped fingernails"></div>
    <div class="sign-photo" style="left:128px;top:6px;width:72px;height:58px;background:linear-gradient(180deg,#e2b7aa,#c88a7e)" role="img" aria-label="Photo of a pale lower eyelid"></div>
    <div class="sign-photo" style="left:204px;top:6px;width:78px;height:58px;background:linear-gradient(180deg,#e8d2c6,#c9a595)" role="img" aria-label="Photo of a pale eye"></div>
    <div class="sign-photo" style="left:8px;top:72px;width:112px;height:80px;background:linear-gradient(180deg,#d8b6a6,#a98376)" role="img" aria-label="Photo of pale hands"></div>
    <div class="sign-photo" style="left:128px;top:72px;width:154px;height:80px;background:linear-gradient(90deg,#c7897c,#e0aba3 50%,#c38478)" role="img" aria-label="Photo of a pale, smooth tongue"></div>
  </div>

  <svg class="rest-scene" viewBox="0 0 523 674" role="img" aria-label="Photo of a tired woman resting in bed with her hand on her forehead">
    <path d="M120 658C170 520 300 432 523 420V658Z" fill="url(#restTone)"/>
    <path d="M0 540C60 520 100 560 120 658H0Z" fill="var(--red)"/>
    <path d="M110 658C160 510 300 418 523 404" fill="none" stroke="var(--red)" stroke-width="14"/>
  </svg>

  <div class="back-strip"></div>
</section>

</body>
</html>
```